Commercial painting company is looking for a creative website designer.

Hi, we just completed our logo project and now ready to launch our website. The project will be done on Squarespace platform. It will contain:
Page 1 HOME
Page 2 SERVICES
Page 3 PICTURES
The content will be written by us. I am not sure bout the pictures, I do not have any to provide. I can buy stock photos if needed.
We are commercial only painting company and have to appeal to commercial, industrial property mangers. We will need CALL, REQUEST FOR ESTIMATE buttons.
If possible to have a live picture on home page would be great. Thank you
Target Market(s)
Property Managers
Industry/Entity Type
Commercial Painting
Other font styles liked:
- Poppins

```html
<!DOCTYPE html>
<html lang="en">
<head>
<meta charset="utf-8">
<title>Summit Coat USA – Commercial Painting</title>
<link href="https://fonts.googleapis.com/css2?family=Poppins:ital,wght@0,400;0,500;0,600;0,700;0,800;1,400&display=swap" rel="stylesheet">
<style>
:root{
  --navy:#0d2a6e;
  --navy-deep:#0a2260;
  --red:#c8102e;
  --red-soft:#d0203f;
  --white:#ffffff;
  --ink:#333333;
  --muted:#555555;
  --rule:#bbbbbb;
}
*{margin:0;padding:0;box-sizing:border-box}
html,body{width:1200px;height:4000px;overflow:hidden;background:var(--white);font-family:'Poppins',sans-serif;color:var(--ink)}
.page{position:relative;width:1200px;height:4000px}
.abs{position:absolute}
.btn{position:absolute;display:flex;align-items:center;justify-content:center;background:var(--red);color:var(--white);font-weight:600;font-size:14px;text-transform:uppercase;letter-spacing:.2px}
.btn.navy{background:var(--navy)}

/* top bar + header */
.topbar{left:0;top:0;width:1200px;height:47px;background:var(--navy)}
.topbar .call{position:absolute;left:636px;top:0;height:47px;display:flex;align-items:center;gap:8px;color:var(--white);font-weight:600;font-size:15px}
.topbar .call .dot{width:22px;height:22px;border-radius:50%;background:var(--red);display:flex;align-items:center;justify-content:center}
.topbar .btn{left:844px;top:0;width:206px;height:47px}
.header{left:0;top:47px;width:1200px;height:83px;background:var(--white)}
.brand{position:absolute;left:150px;top:14px;width:190px;height:190px;border-radius:50%;background:var(--white);border:5px solid var(--navy);display:flex;align-items:center;justify-content:center;z-index:5}
.brand span{font-weight:700;font-size:22px;color:var(--navy);text-align:center;line-height:1.15}
.nav{position:absolute;top:47px;height:83px;left:515px;display:flex;align-items:center;gap:58px;font-size:15px;font-weight:500;color:var(--navy-deep)}
.nav .active{color:var(--red);font-weight:600}

/* hero */
.hero-photo{left:0;top:130px;width:1200px;height:605px;background:linear-gradient(100deg,#8e9aa6 0%,#c7ccc9 22%,#5c7fa8 48%,#1f4f8f 75%,#2a3d5c 100%)}
.hero-title{left:665px;top:292px;color:var(--white);font-weight:800;line-height:1.12}
.hero-title .l1{font-size:60px;display:block}
.hero-title .l2{font-size:48px;display:block}
.hero .btn{top:492px;height:44px}

/* blue intro band */
.intro{left:0;top:735px;width:1200px;height:395px;background:linear-gradient(120deg,#14347e 0%,var(--navy) 40%,var(--navy-deep) 100%)}
.intro p{position:absolute;left:150px;width:900px;top:100px;text-align:center;color:var(--white);font-weight:600;font-size:29px;line-height:1.22}

/* commercial painting */
.section-title{font-weight:800;font-size:41px;line-height:1.04;text-transform:uppercase}
.section-title .blue{color:var(--navy)}
.section-title .red{color:var(--red);display:block}
.body-copy{font-size:15px;line-height:1.42;color:var(--muted)}
.commercial .section-title{position:absolute;left:150px;top:1310px}
.commercial .body-copy{position:absolute;left:150px;top:1414px;width:390px}
.commercial .btn{left:150px;top:1569px;width:126px;height:46px;font-size:13px}
.commercial-photo{left:570px;top:1255px;width:534px;height:430px;background:linear-gradient(160deg,#c9cdd2 0%,#e4e6e8 45%,#8a96a4 100%)}

/* completed projects */
.projects-photo{left:0;top:1834px;width:1200px;height:575px;background:linear-gradient(180deg,#4d8fd8 0%,#8fbbe8 45%,#d9c2a0 60%,#9a9a96 85%,#c4c4bf 100%)}
.projects-card{left:683px;top:2152px;width:517px;height:202px;background:rgba(200,16,46,.86);color:var(--white)}
.projects-card h3{position:absolute;left:48px;top:56px;font-size:26px;font-weight:700;letter-spacing:.3px}
.projects-card p{position:absolute;left:43px;top:98px;width:350px;font-size:18px;font-weight:600;line-height:1.3}
.projects-card svg{position:absolute;left:425px;top:90px}

/* about */
.about-ring{left:120px;top:2555px;width:506px;height:506px;border-radius:50%;border:3px solid var(--navy)}
.about-ring-red{left:138px;top:2573px;width:470px;height:470px;border-radius:50%;border:3px solid var(--red)}
.about-photo{left:153px;top:2588px;width:440px;height:440px;border-radius:50%;background:radial-gradient(circle at 60% 45%,#e8c46a 0%,#d9a941 40%,#9aa0a6 75%,#6e767e 100%)}
.about .section-title{position:absolute;left:669px;top:2636px}
.about .body-copy{position:absolute;left:669px;top:2740px;width:390px}
.about .btn{left:669px;top:2894px;width:126px;height:46px;font-size:13px}

/* testimonial */
.testimonial{left:0;top:3153px;width:1200px;height:486px;background:var(--navy)}
.testimonial .quote-bg{position:absolute;left:0;top:60px;font-size:380px;line-height:1;font-weight:800;color:rgba(255,255,255,.04)}
.testimonial .mark{position:absolute;color:var(--white);font-size:70px;font-weight:800;font-style:italic;line-height:1}
.testimonial blockquote{position:absolute;left:178px;top:152px;width:520px;color:var(--white);font-style:italic;font-size:22px;line-height:1.38}
.testimonial .author{position:absolute;left:173px;top:300px;color:var(--red);font-size:25px}
.client-photo{left:775px;top:3273px;width:227px;height:227px;border-radius:50%;background:radial-gradient(circle at 50% 40%,#e9e9eb 0%,#cfd1d6 60%,#a7abb3 100%)}
.quote-badge{left:931px;top:3414px;width:86px;height:86px;border-radius:50%;background:var(--red);display:flex;align-items:center;justify-content:center;color:var(--white);font-size:56px;font-weight:800;line-height:1;padding-top:22px}

/* footer */
.footer-brand{left:525px;top:3590px;width:150px;height:150px;border-radius:50%;background:var(--white);border:4px solid var(--navy);display:flex;align-items:center;justify-content:center}
.footer-brand span{font-weight:700;font-size:17px;color:var(--navy);text-align:center;line-height:1.15}
.contacts{left:0;top:3782px;width:1200px;display:flex;justify-content:center;gap:38px;padding-left:30px}
.contact{display:flex;align-items:center;gap:6px;font-size:17px;line-height:1.1;color:var(--ink)}
.contact .ic{width:40px;height:40px;border-radius:50%;background:var(--red);display:flex;align-items:center;justify-content:center}
.contact .val{margin-top:0}
.rule{left:248px;top:3867px;width:701px;height:1px;background:var(--rule)}
.copyright{left:0;top:3896px;width:1200px;text-align:center;font-size:14px;color:var(--ink)}
.social{left:0;top:3937px;width:1200px;display:flex;justify-content:center;gap:22px}
.social span{width:22px;height:22px;border-radius:50%;background:var(--navy)}
.social span.red{background:var(--red)}
</style>
</head>
<body>
<div class="page">

  <!-- top bar -->
  <div class="abs topbar">
    <div class="call">
      <span class="dot"><svg width="12" height="12" viewBox="0 0 24 24"><path fill="#fff" d="M6.6 10.8a15.1 15.1 0 0 0 6.6 6.6l2.2-2.2c.3-.3.7-.4 1-.2 1.1.4 2.3.6 3.6.6.6 0 1 .4 1 1V20c0 .6-.4 1-1 1A17 17 0 0 1 3 4c0-.6.4-1 1-1h3.5c.6 0 1 .4 1 1 0 1.3.2 2.5.6 3.6.1.3 0 .7-.2 1z"/></svg></span>
      CALL: (123) 345 6789
    </div>
    <div class="btn">Request for estimate</div>
  </div>

  <header class="abs header"></header>
  <div class="brand"><span>Summit Coat<br>USA</span></div>
  <nav class="nav">
    <span class="active">HOME</span>
    <span>SERVICES</span>
    <span>COMPLETED PROJECTS</span>
    <span>CONTACT</span>
  </nav>

  <!-- hero -->
  <section class="hero">
    <div class="abs hero-photo" role="img" aria-label="Rope-access painter in a hard hat carrying a paint bucket down a glass and concrete commercial facade"></div>
    <h1 class="abs hero-title"><span class="l1">The Best</span><span class="l2">Commercial</span><span class="l2">Painting Solution!</span></h1>
    <div class="btn" style="left:666px;width:203px">Request for estimate</div>
    <div class="btn navy" style="left:879px;width:103px">Call us</div>
  </section>

  <!-- intro band -->
  <section class="abs intro">
    <p>Lorem ipsum dolor sit amet, consectetur adipiscing elit, sed do eiusmod tempor incididunt ut labore et dolore magna aliquauis ipsum suspendisse</p>
    <div class="btn" style="left:499px;top:242px;width:202px;height:46px">Request for estimate</div>
  </section>

  <!-- commercial painting -->
  <section class="commercial">
    <h2 class="section-title"><span class="blue">Commercial</span><span class="red">Painting</span></h2>
    <p class="body-copy">Lorem ipsum dolor sit amet, consectetur adipiscing elit, sed do eiusmod tempor incididunt ut labore et dolore magna aliqua. Ut enim ad minim veniam, quis nostrud exercitation ullamco laboris nisi ut aliquip ex ea commodo consequat. Duis aute irure dolor in reprehenderit in voluptate velit.</p>
    <div class="btn">Read more</div>
    <div class="abs commercial-photo" role="img" aria-label="Two painters in harnesses painting the white wall of a building beside tall windows"></div>
  </section>

  <!-- completed projects -->
  <section>
    <div class="abs projects-photo" role="img" aria-label="Freshly painted single-storey retail building with glass storefronts under a blue sky"></div>
    <div class="abs projects-card">
      <h3>COMPLETED PROJECTS</h3>
      <p>Lorem ipsum dolor sit amet consect etur adipiscing eluincididun</p>
      <svg width="28" height="22" viewBox="0 0 28 22"><path d="M11 3 3 11l8 8M17 3l8 8-8 8" fill="none" stroke="#fff" stroke-width="3"/></svg>
    </div>
  </section>

  <!-- about -->
  <section class="about">
    <div class="abs about-ring"></div>
    <div class="abs about-ring-red"></div>
    <div class="abs about-photo" role="img" aria-label="Painter on ropes rolling yellow paint onto an exterior wall"></div>
    <h2 class="section-title"><span class="blue">About</span><span class="red">Summit Coat USA</span></h2>
    <p class="body-copy">Lorem ipsum dolor sit amet, consectetur adipiscing elit, sed do eiusmod tempor incididunt ut labore et dolore magna aliqua. Ut enim ad minim veniam, quis nostrud exercitation ullamco laboris nisi ut aliquip ex ea commodo consequat. Duis aute irure dolor in reprehenderit in voluptate velit.</p>
    <div class="btn">Read more</div>
  </section>

  <!-- testimonial -->
  <section class="abs testimonial">
    <div class="quote-bg">&ldquo;</div>
    <div class="mark" style="left:135px;top:130px">&ldquo;</div>
    <blockquote>Lorem ipsum dolor sit amet, consectetur adipiscing elit, sed do eiusmod tempor incididunt ut labore et dolore magna aliqua. Quis ipsum suspendisse ultrices gravida.</blockquote>
    <div class="mark" style="left:490px;top:248px">&rdquo;</div>
    <div class="author">Marla Quinton</div>
  </section>
  <div class="abs client-photo" role="img" aria-label="Portrait of a satisfied client"></div>
  <div class="abs quote-badge">&ldquo;</div>

  <!-- footer -->
  <div class="abs footer-brand"><span>Summit Coat<br>USA</span></div>
  <div class="abs contacts">
    <div class="contact">
      <span class="ic"><svg width="18" height="14" viewBox="0 0 18 14"><rect x="0" y="0" width="18" height="14" rx="2" fill="#fff"/><path d="M1 1l8 6 8-6" fill="none" stroke="#c8102e" stroke-width="1.6"/></svg></span>
      <span>Email:<br>info@company.com</span>
    </div>
    <div class="contact">
      <span class="ic"><svg width="18" height="18" viewBox="0 0 24 24"><path fill="#fff" d="M6.6 10.8a15.1 15.1 0 0 0 6.6 6.6l2.2-2.2c.3-.3.7-.4 1-.2 1.1.4 2.3.6 3.6.6.6 0 1 .4 1 1V20c0 .6-.4 1-1 1A17 17 0 0 1 3 4c0-.6.4-1 1-1h3.5c.6 0 1 .4 1 1 0 1.3.2 2.5.6 3.6.1.3 0 .7-.2 1z"/></svg></span>
      <span>Phone:<br>989 xx x7868</span>
    </div>
    <div class="contact">
      <span class="ic"><svg width="16" height="20" viewBox="0 0 16 20"><path d="M8 0a8 8 0 0 0-8 8c0 6 8 12 8 12s8-6 8-12a8 8 0 0 0-8-8z" fill="#fff"/><circle cx="8" cy="8" r="3" fill="#c8102e"/></svg></span>
      <span>Address:<br>Lorem dumy text 098</span>
    </div>
  </div>
  <div class="abs rule"></div>
  <div class="abs copyright">Copyrights © 2023 All rights are reserved.</div>
  <div class="abs social" aria-label="Social media links">
    <span></span><span class="red"></span><span></span>
  </div>

</div>
</body>
</html>
```